TRELLWICK Construction Group business card for distribution

A business card detailing our services, with our phone number and email address.
- Groundworks / Foundations / Drainage
- Landscaping / Hard Landscaping / Patios / Decking
- Fencing
The card should include company logo and be in the same colours.

Target Market(s)
Domestic Houses
Industry/Entity Type
Construction
Contact Information for Business Card
Phone Number - 07931 258 904 / 07713829516. Email address: trellgroup@stonevane-mail.com
Font styles to use
Serif
Sans Serif
Colors
F0912C
F2A743
F7CA91
FBE8D2
FDF5EE
Requirements
Must have
- Contact numbers. Photos of past work. Company Logo

Nice to have
- Company Logo

```html
<!DOCTYPE html>
<html lang="en">
<head>
<meta charset="utf-8">
<title>TRELLWICK Construction Group – Business Card</title>
<link rel="stylesheet" href="https://fonts.googleapis.com/css2?family=Montserrat:wght@400;500;600;700&family=Arimo:wght@400&display=swap">
<style>
  :root {
    --canvas: #2a2a2d;
    --card: #050505;
    --orange: #f0912c;
    --orange-soft: #f2a743;
    --white: #ffffff;
    --grey-band: #c9c9c9;
    --photo-a: #8a8f92;
    --photo-b: #6f7a5c;
    --photo-c: #a8895f;
    --photo-d: #9a9b96;
  }
  * { margin: 0; padding: 0; box-sizing: border-box; }
  html, body { width: 1200px; height: 900px; overflow: hidden; }
  body {
    background: var(--canvas);
    font-family: "Montserrat", Arial, sans-serif;
    position: relative;
  }
  .card {
    position: absolute;
    left: 290px;
    width: 620px;
    height: 354px;
    background: var(--card);
    border-radius: 22px;
    overflow: hidden;
  }
  .card--front { top: 76px; }
  .card--back { top: 470px; }

  /* Front */
  .work-gallery {
    position: absolute;
    top: 0; left: 0; right: 0;
    height: 196px;
    display: flex;
    gap: 8px;
    padding: 0;
  }
  .work-photo { flex: 1; height: 100%; }
  .work-photo--yard { background: linear-gradient(180deg, #a9c4dc 0%, var(--photo-a) 45%, #55585a 100%); }
  .work-photo--path { background: linear-gradient(180deg, #7f9a5a 0%, var(--photo-b) 40%, #5e5a52 100%); }
  .work-photo--deck { background: linear-gradient(180deg, #c9ccd0 0%, var(--photo-c) 45%, #8a6f4a 100%); }
  .work-photo--slab { background: linear-gradient(180deg, #b7bcc2 0%, var(--photo-d) 50%, #7c7b74 100%); }

  .services-band {
    position: absolute;
    top: 196px; left: 0; right: 0;
    height: 42px;
    background: var(--orange);
    display: flex; align-items: center; justify-content: center;
  }
  .services-title {
    font-weight: 700;
    font-size: 26px;
    letter-spacing: 7px;
    color: #000;
  }
  .services-list {
    position: absolute;
    top: 256px; left: 0; right: 0;
    text-align: center;
    font-family: "Arimo", Arial, sans-serif;
    color: var(--white);
    font-size: 22px;
    line-height: 30px;
  }

  /* Back */
  .brand {
    position: absolute;
    top: 44px; right: 46px;
    text-align: right;
    color: var(--white);
  }
  .brand-mark {
    display: flex; align-items: center; justify-content: flex-end; gap: 10px;
  }
  .brand-square { width: 22px; height: 22px; background: var(--orange); }
  .brand-name { font-weight: 700; font-size: 40px; letter-spacing: 1px; }
  .brand-sub { font-weight: 600; font-size: 14px; letter-spacing: 2px; margin-top: 4px; }

  .divider { position: absolute; }
  .address {
    position: absolute;
    top: 156px; right: 46px;
    text-align: right;
    color: var(--white);
    font-size: 15px;
    line-height: 22px;
  }
  .person {
    position: absolute;
    left: 40px; top: 176px;
  }
  .person-name { color: var(--orange); font-weight: 600; font-size: 27px; letter-spacing: 0.5px; }
  .person-role { color: var(--white); font-size: 17px; margin-top: 2px; }
  .person-rule { width: 300px; height: 1.5px; background: var(--orange); margin-top: 10px; }
  .contact-list { list-style: none; margin-top: 8px; }
  .contact-item {
    display: flex; align-items: center; gap: 10px;
    color: var(--white); font-size: 15px; line-height: 22px;
  }
  .contact-icon { width: 16px; height: 16px; flex: none; }
  .edge-band {
    position: absolute; left: 0; right: 0; bottom: 0; height: 12px;
    display: flex;
  }
  .edge-band__grey { flex: 7; background: var(--grey-band); }
  .edge-band__orange { flex: 3; background: var(--orange); }
</style>
</head>
<body>

<section class="card card--front" aria-label="Card front">
  <div class="work-gallery">
    <div class="work-photo work-photo--yard" role="img" aria-label="Photo of a finished concrete yard beside a building"></div>
    <div class="work-photo work-photo--path" role="img" aria-label="Photo of a garden path with new fencing"></div>
    <div class="work-photo work-photo--deck" role="img" aria-label="Photo of new timber decking in a back garden"></div>
    <div class="work-photo work-photo--slab" role="img" aria-label="Photo of a new concrete slab outside a unit"></div>
  </div>
  <div class="services-band"><h2 class="services-title">OUR SERVICES</h2></div>
  <p class="services-list">Groundworks / Foundations / Drainage- Landscaping<br>/ Hard Landscaping / Patios / Decking</p>
</section>

<section class="card card--back" aria-label="Card back">
  <div class="brand">
    <div class="brand-mark">
      <span class="brand-name">TRELLWICK</span>
      <span class="brand-square"></span>
    </div>
    <div class="brand-sub">CONSTRUCTION GROUP LTD</div>
  </div>

  <svg class="divider" width="620" height="354" viewBox="0 0 620 354" style="left:0;top:0">
    <line x1="300" y1="144" x2="580" y2="144" stroke="var(--orange)" stroke-width="1.5"/>
  </svg>

  <p class="address">421, Address line goes here<br>45452, Country name</p>

  <div class="person">
    <h1 class="person-name">DANIEL WHITCOMBE</h1>
    <p class="person-role">Owner</p>
    <div class="person-rule"></div>
    <ul class="contact-list">
      <li class="contact-item">
        <svg class="contact-icon" viewBox="0 0 16 16"><circle cx="8" cy="8" r="8" fill="var(--orange)"/><path d="M5 4.5l1.6-.3.8 2-1 .8a5 5 0 0 0 2.6 2.6l.8-1 2 .8-.3 1.6c-3.6.3-6.8-2.9-6.5-6.5z" fill="#000"/></svg>
        07931 258 904 / 07713829516
      </li>
      <li class="contact-item">
        <svg class="contact-icon" viewBox="0 0 16 16"><rect x="1" y="3" width="14" height="10" rx="1" fill="var(--orange)"/><path d="M1.5 3.8L8 9l6.5-5.2" stroke="#000" stroke-width="1.4" fill="none"/></svg>
        trellgroup@stonevane-mail.com
      </li>
      <li class="contact-item">
        <svg class="contact-icon" viewBox="0 0 16 16"><circle cx="8" cy="8" r="7.5" fill="var(--orange)"/><path d="M3 6h10M3 10h10M8 1c-3 3.5-3 10.5 0 14M8 1c3 3.5 3 10.5 0 14" stroke="#000" stroke-width="1" fill="none"/></svg>
        www.trellwickgroup.com
      </li>
    </ul>
  </div>

  <div class="edge-band"><span class="edge-band__grey"></span><span class="edge-band__orange"></span></div>
</section>

</body>
</html>
```